Landing Page Design

This project needs landing page desing only. However, whoever wins this round will get to work directly on all other pages of the website as a separate private project.

See attached file for more details.

Target Market(s)

25-60 year old person who is looking for health insurance quotes.

Industry/Entity Type

Health Insurance

Number of Pages Required

1 page

Font styles to use
Sans Serif

Requirements
Must have
• see attachment
Nice to have
• see attachment
Should not have
• see attachment

```html
<!DOCTYPE html>
<html lang="en">
<head>
<meta charset="utf-8">
<title>CoverBridgeRates.com – Compare 2016 Health Insurance Plans</title>
<link href="https://fonts.googleapis.com/css2?family=Lato:wght@400;700;900&display=swap" rel="stylesheet">
<style>
  :root{
    --teal:#33b3d6;
    --navy:#0f2d4f;
    --navy-deep:#0a2444;
    --red:#9b1406;
    --red-text:#c0170a;
    --orange:#f7941d;
    --cyan:#2bc3ef;
    --text:#555b61;
    --white:#ffffff;
    --table-blue:#1b84c4;
  }
  *{box-sizing:border-box;margin:0;padding:0}
  html,body{width:1200px;height:1200px;overflow:hidden}
  body{font-family:'Lato',sans-serif;background:var(--white);position:relative;color:var(--text)}

  .site-header{position:absolute;left:0;top:0;width:1200px;height:68px;background:var(--teal);border-top:3px solid var(--navy);border-bottom:3px solid #7fd0e8}
  .brand{position:absolute;left:153px;top:14px;display:flex;align-items:center;gap:6px}
  .brand-mark{width:28px;height:28px;background:var(--navy);border-radius:50%}
  .brand-name{color:var(--white);font-weight:700;font-size:21px;line-height:1}
  .brand-tag{color:var(--white);font-size:6px;letter-spacing:2px;font-weight:700;text-transform:uppercase;margin-top:2px}
  .call-box{position:absolute;left:869px;top:9px;width:177px;height:48px;background:var(--white);border-radius:3px;display:flex;align-items:center}
  .call-photo{width:48px;height:48px;background:linear-gradient(135deg,#d8d8d8,#6b6b6b);border-radius:3px 0 0 3px}
  .call-text{margin-left:3px;color:var(--red-text);font-weight:900;font-size:12.5px;line-height:15px}

  .hero{position:absolute;left:0;top:68px;width:1200px;height:404px;background:linear-gradient(180deg,#cfd2d4 0%,#dcdfe0 45%,#e7e8e9 100%)}
  .hero-title{position:absolute;left:0;width:1200px;top:44px;text-align:center;font-size:43px;color:var(--navy);font-weight:400;letter-spacing:-.5px}
  .hero-title em{font-style:normal;font-weight:900;color:var(--red-text)}
  .hero-lead{position:absolute;left:300px;width:600px;top:110px;text-align:center;font-size:13.5px;line-height:18.5px;color:#222}
  .hero-people{position:absolute;left:878px;top:100px;width:148px;height:304px;background:linear-gradient(180deg,#c9a58a 0%,#6f9fd6 40%,#c98c2b 100%);border-radius:70px 70px 0 0;opacity:.85}
  .quote-box{position:absolute;left:364px;top:178px;width:472px;height:138px;background:var(--red);border:3px solid #b63022;outline:1px solid #d97a70}
  .quote-title{position:absolute;top:22px;width:100%;text-align:center;color:var(--white);font-weight:900;font-size:19px}
  .zip{position:absolute;left:30px;top:60px;width:143px;height:41px;background:var(--white);border-radius:2px;display:flex;align-items:center;padding-left:10px;gap:8px;font-size:11.5px;color:#8a8a8a}
  .submit{position:absolute;left:178px;top:60px;width:86px;height:41px;background:var(--orange);color:var(--white);font-weight:900;font-size:15px;display:flex;align-items:center;justify-content:center;border-radius:2px}
  .or{position:absolute;left:278px;top:70px;color:var(--white);font-size:15px}
  .agent{position:absolute;left:306px;top:60px;width:126px;height:41px;border:2px solid var(--white);color:var(--white);font-weight:700;font-size:12.5px;display:flex;align-items:center;justify-content:center;border-radius:2px}
  .carriers{position:absolute;left:432px;top:344px;display:flex;gap:22px;align-items:center}
  .carrier{height:22px;background:#6d7074;border-radius:4px;opacity:.75}

  .info{position:absolute;top:472px;left:0;width:1200px;height:348px}
  .info-col{position:absolute;top:40px}
  .info-col h3{font-size:13.6px;font-weight:700;color:var(--navy);margin-bottom:14px;white-space:nowrap}
  .info-img{width:274px;height:90px;border:1px solid #d4d4d4;padding:3px;margin-left:-3px}
  .info-img div{width:100%;height:100%}
  .info-col p{margin-top:16px;font-size:11.2px;line-height:15.2px;color:var(--text)}
  .more{color:var(--red-text)}

  .plans{position:absolute;top:820px;left:0;width:1200px;height:380px;background:radial-gradient(circle at 70% 40%,#153d66 0%,var(--navy-deep) 70%)}
  .plans h2{position:absolute;left:156px;top:88px;font-size:28px;font-weight:700;color:var(--cyan);letter-spacing:-.3px}
  .plans p{position:absolute;left:156px;top:140px;width:340px;font-size:11.4px;line-height:16px;color:var(--white)}
  .plans-btn{position:absolute;left:152px;top:254px;width:220px;height:46px;border:2px solid var(--white);border-radius:3px;color:var(--white);font-weight:700;font-size:11.2px;display:flex;align-items:center;justify-content:center;white-space:nowrap}
  .plan-table{position:absolute;left:640px;top:150px;width:420px;border-collapse:collapse;background:var(--white);font-family:'Lato',sans-serif}
  .plan-table th{background:var(--table-blue);color:var(--white);font-weight:900;font-size:15px;height:42px;text-align:left;padding-left:10px}
  .plan-table th.col,.plan-table td.col{text-align:center;padding-left:0;width:70px}
  .plan-table td{height:38px;font-size:11px;font-weight:700;color:#333;padding-left:10px;border-bottom:1px solid #e6e6e6}
  .plan-table td.col{background:#f0f2f4}
</style>
</head>
<body>
  <header class="site-header">
    <div class="brand">
      <div class="brand-mark"></div>
      <div>
        <div class="brand-name">CoverBridgeRates.com</div>
        <div class="brand-tag">Clear answers on health coverage</div>
      </div>
    </div>
    <div class="call-box">
      <div class="call-photo" role="img" aria-label="Photo of a support agent wearing a headset"></div>
      <div class="call-text">CALL FOR QUOTES:<br>(800) 555-0142</div>
    </div>
  </header>

  <section class="hero" role="img" aria-label="Faded photo of a couple at the seaside">
    <h1 class="hero-title">Compare <em>2016</em> Health Insurance Plans</h1>
    <p class="hero-lead">Neque porro quisquam est qui dolorem ipsum quia dolor sit amet, consectetur, adipisci velit.<br>There is no one who loves pain itself, who seeks after it and wants to have it,</p>
    <div class="hero-people" role="img" aria-label="Photo of a smiling young couple"></div>
    <div class="quote-box">
      <div class="quote-title">GET YOUR FREE QUOTES NOW!</div>
      <div class="zip">
        <svg width="16" height="16" viewBox="0 0 16 16"><circle cx="6.5" cy="6.5" r="4.5" fill="none" stroke="#999" stroke-width="1.6"/><line x1="10" y1="10" x2="14.5" y2="14.5" stroke="#999" stroke-width="2"/></svg>
        Enter ZIP CODE
      </div>
      <div class="submit">SUBMIT</div>
      <div class="or">OR</div>
      <div class="agent">CALL TO AGENT</div>
    </div>
    <div class="carriers">
      <div class="carrier" style="width:70px"></div>
      <div class="carrier" style="width:52px"></div>
      <div class="carrier" style="width:78px"></div>
      <div class="carrier" style="width:82px"></div>
    </div>
  </section>

  <section class="info">
    <article class="info-col" style="left:154px;width:262px">
      <h3>How do I Buy Health Insurance?</h3>
      <div class="info-img"><div role="img" aria-label="Photo of a health insurance policy under a magnifying glass" style="background:linear-gradient(135deg,#9aa5ad,#eef1f3 60%,#b8c2c9)"></div></div>
      <p>For some, buying health insurance can be a confusing and overwhelming process. First, you have to find a health insurance plan within your budget. Then you have to contact the company or an insurance agent in order to get a quote. Once you have all of that information, you can evaluate your options.<br><span class="more">[ continue reading + ]</span></p>
    </article>
    <article class="info-col" style="left:469px;width:270px">
      <h3>What is the Healthcare Marketplace?</h3>
      <div class="info-img"><div role="img" aria-label="Illustration of a laptop showing a health insurance marketplace" style="background:#f0b323"></div></div>
      <p>The passage of the Affordable Care Act established the Healthcare Marketplace. There are two distinct divisions - a state level, and a federal level. 37 states are members of the federal exchange, and 14 are limited to a state exchange. Unfortunately, not all insurance companies are required to provide information <span class="more">[ continue reading + ]</span></p>
    </article>
    <article class="info-col" style="left:797px;width:264px">
      <h3>What’s the "Health Insurance Exchange"?</h3>
      <div class="info-img"><div role="img" aria-label="Photo of letter blocks spelling health care" style="background:linear-gradient(90deg,#d9312a 0 18%,#2a86c8 18%)"></div></div>
      <p>The Health Insurance Exchange is the pool of health care plans and providers which are cooperating with the federal government in order to provide affordable health insurance to Americans in many states. 37 states are members of the Exchange on the federal level: AL, AK, AZ, AK, DE, FL, GA, HI, IL, IN, IA, KS, LA, ME, MI, MS, MO, MT, NE, NV, NH, NJ, NM, NC, ND,<br><span class="more">[ continue reading + ]</span></p>
    </article>
  </section>

  <section class="plans">
    <h2>Health Insurance Plan Types</h2>
    <p>Lorem Ipsum is simply dummy text of the printing and typesetting industry. Lorem Ipsum has been the industry's standard dummy text ever since the 1500s, when an unknown printer took a galley of type and scrambled it to make a type specimen book. It has survived not only five centuries, but also the leap into electronic typesetting, remaining essentially unchanged.</p>
    <div class="plans-btn">VIEW THE HEALTH INSURANCE PLAN</div>
    <table class="plan-table">
      <tr><th>PLAN TYPES</th><th class="col">PPO</th><th class="col">EPO</th></tr>
      <tr><td>PCP Required?</td><td class="col">NO</td><td class="col">NO</td></tr>
      <tr><td>Referrals Required?</td><td class="col">NO</td><td class="col">NO</td></tr>
      <tr><td>Pre-Authorization Required?</td><td class="col">YES</td><td class="col">YES</td></tr>
      <tr><td>Out-of-Network Coverage?</td><td class="col">YES</td><td class="col">NO</td></tr>
    </table>
  </section>
</body>
</html>
```